Vornique Business Cards

We need new business cards that incorporate our new compnay logo and color scheme. We are a custom publishing company located in Ann Arbor, MI.

Target Market(s)

Deans, Assistant Deans, Executive MBA Program Directors and Faculty at top universities in North America. Top publishers in North America.

Industry/Entity Type

Publishing Company

Requirements
Must have
• The Vornique Logo
The following color palatte:
Gold:
C: 1
M: 6
Y: 25
K: 0

Darker gold
C: 0
M: 31
Y: 100
K: 0

Purple
C: 78
M: 100
Y: 0
K: 33

Teal
C: 87
M: 0
Y: 38
K: 0

Must also be able to fit the following sample b-card information:
www.vornique-example.com
Priya Ostrander
Director, Marketing
2315 Harrow Lane, PO Box 417
Corvell, MN 55213-0417
phone: 800-555-0143 x2291
email: postrander@vornique-example.com
Nice to have
• match the look and feel of our website: www.vornique-example.com

```html
<!DOCTYPE html>
<html lang="en">
<head>
<meta charset="utf-8">
<title>Vornique Business Card</title>
<link rel="stylesheet" href="https://fonts.googleapis.com/css2?family=Alegreya+Sans:wght@400;700&display=swap">
<style>
  :root {
    --purple: #4a1a6b;
    --gold-light: #fdf0c8;
    --gold-dark: #fbb217;
    --teal: #1fb6a8;
    --text-light: #e6dcef;
    --page: #ffffff;
  }
  * { margin: 0; padding: 0; box-sizing: border-box; }
  html, body {
    width: 1200px;
    height: 900px;
    overflow: hidden;
    background: var(--page);
  }
  .business-card {
    position: absolute;
    left: 28px;
    top: 114px;
    width: 1144px;
    height: 656px;
    background: var(--purple);
    overflow: hidden;
    font-family: "Alegreya Sans", sans-serif;
  }
  .card-wave {
    position: absolute;
    inset: 0;
    width: 100%;
    height: 100%;
  }
  .wave-stripe { fill: var(--gold-dark); }
  .wave-panel { fill: var(--gold-light); }
  .contact-block {
    position: absolute;
    left: 40px;
    top: 350px;
  }
  .person-name {
    color: var(--gold-dark);
    font-weight: 700;
    font-size: 38px;
    line-height: 40px;
    letter-spacing: 0.5px;
  }
  .person-title {
    color: var(--gold-dark);
    font-weight: 700;
    font-size: 31px;
    line-height: 36px;
    margin-bottom: 10px;
  }
  .contact-lines {
    list-style: none;
    color: var(--text-light);
    font-size: 30px;
    line-height: 37.5px;
    letter-spacing: 0.3px;
  }
  .brand-mark {
    position: absolute;
    left: 790px;
    top: 540px;
    display: flex;
    align-items: center;
    gap: 14px;
  }
  .brand-dot {
    width: 34px;
    height: 34px;
    border-radius: 50%;
    background: var(--purple);
  }
  .brand-name {
    color: var(--teal);
    font-weight: 700;
    font-size: 58px;
    line-height: 1;
  }
</style>
</head>
<body>
  <section class="business-card">
    <svg class="card-wave" viewBox="0 0 1144 656" preserveAspectRatio="none" aria-hidden="true">
      <path class="wave-stripe" d="M410,656 C680,592 850,400 872,150 C878,80 910,18 968,0 L1144,0 L1144,656 Z"/>
      <path class="wave-panel" d="M446,656 C705,600 888,405 904,155 C910,85 938,22 992,0 L1144,0 L1144,656 Z"/>
    </svg>

    <div class="contact-block">
      <h1 class="person-name">Priya Ostrander</h1>
      <p class="person-title">Director, Marketing</p>
      <ul class="contact-lines">
        <li>2315 Harrow Lane, PO Box 417</li>
        <li>Corvell, MN 55213 - 0417</li>
        <li>Phone: 800 - 555 - 0143 x2291</li>
        <li>E-mail: postrander@vornique-example.com</li>
        <li>www.vornique-example.com</li>
      </ul>
    </div>

    <div class="brand-mark">
      <span class="brand-dot"></span>
      <span class="brand-name">Vornique</span>
    </div>
  </section>
</body>
</html>
```